Harbourline Metro Business Racquet Circuit (est.1952)

The Metro Business Racquet Circuit began in 1952 and has been played every year since. It is the longest running continuous sporting competition in the Sydney CBD. It is a team squash competition from May to Oct yearly played between companies, sporting groups or just a groups of friends.
We are looking for a flyer that we can reuse every year (so the content within the flyer can't be tied to a specific time). Other specific we are looking for are
1. Squash imagery (can either be real or graphic design) depicting action / athleticism / friendly rivalry
2. Needs the following content
a ) "A Sydney CBD based competition for friendly rivalry between companies, sporting clubs or between friends"
b) "All matches in and around the CBD from 5.30pm to 8pm"
c) "We cater for all playing abilities"
d) "Ladies beginner comp includes complimentary coaching"
e) "Visit our website www.plvqn.org.au for more info or contact Walter on frontw@qmx.com.au"

Flyer needs to include the logos attached in file upload section

```html
<!DOCTYPE html>
<html lang="en">
<head>
<meta charset="utf-8">
<title>Metro Business Racquet Circuit – Flyer</title>
<link rel="stylesheet" href="https://fonts.googleapis.com/css2?family=Oswald:wght@500;700&family=Roboto+Condensed:wght@400;700&family=Kalam:wght@700&display=swap">
<style>
  :root {
    --navy: #1d3a72;
    --blue-deep: #1a4a8c;
    --blue-bright: #0f6cb5;
    --yellow: #f4b91c;
    --orange: #f26a1b;
    --white: #ffffff;
    --stage: #a8a8a8;
    --ink-soft: #5a6f95;
  }
  * { box-sizing: border-box; margin: 0; padding: 0; }
  html, body { width: 1200px; height: 900px; overflow: hidden; }
  body {
    background: var(--stage);
    display: flex; align-items: center; justify-content: center;
    font-family: "Roboto Condensed", "Arial Narrow", sans-serif;
  }
  .flyer {
    position: relative; width: 608px; height: 860px;
    background: var(--navy); overflow: hidden;
    box-shadow: 0 8px 24px rgba(0,0,0,.25);
  }
  .flyer-shapes { position: absolute; inset: 0; }

  .player-art {
    position: absolute; left: 235px; top: 262px; width: 373px; height: 328px;
    background: linear-gradient(160deg, #ffffff 0%, #c9d3e6 45%, var(--navy) 100%);
  }

  .headline {
    position: absolute; right: 40px; top: 28px; z-index: 2;
    font-family: "Oswald", "Arial Narrow", sans-serif; font-weight: 700;
    color: var(--white); text-transform: uppercase; text-align: right;
    line-height: .88;
  }
  .headline-kicker { display: block; font-size: 32px; letter-spacing: .5px; margin-bottom: 6px; }
  .headline-main { display: block; font-size: 84px; letter-spacing: 1px; }

  .club-mark {
    position: absolute; left: 36px; top: 226px; z-index: 2;
    display: flex; align-items: center; gap: 8px;
    background: var(--navy); border: 3px solid var(--white);
    border-radius: 10px; padding: 8px 12px;
  }
  .club-mark-dot { width: 22px; height: 22px; border-radius: 50%; background: var(--yellow); }
  .club-mark-name {
    font-family: "Oswald", sans-serif; font-weight: 700; font-size: 20px;
    color: var(--white); text-transform: uppercase;
  }

  .est-tag {
    position: absolute; left: 300px; top: 258px; z-index: 2;
    background: var(--yellow); color: var(--navy);
    font-family: "Kalam", cursive; font-size: 22px;
    padding: 2px 14px; transform: rotate(-6deg);
  }

  .key-points {
    position: absolute; left: 82px; top: 370px; width: 150px;
    list-style: none; color: var(--navy);
    font-family: "Oswald", sans-serif; font-weight: 500;
    font-size: 16px; line-height: 1.05; text-transform: uppercase;
  }
  .key-points li { padding: 12px 0; border-bottom: 2px solid var(--navy); }
  .key-points li:last-child { border-bottom: none; }

  .tagline {
    position: absolute; right: 24px; top: 600px; width: 360px;
    color: var(--white); font-weight: 700; font-size: 22px;
    line-height: 1.13; text-align: right;
  }
  .tagline em { font-style: normal; color: var(--yellow); }

  .info-band { position: absolute; left: 70px; right: 0; top: 728px; color: var(--navy); }
  .info-title {
    font-family: "Oswald", sans-serif; font-weight: 700; font-size: 14px;
    letter-spacing: 6px; text-transform: uppercase; margin-left: 20px;
  }
  .info-contacts { display: flex; gap: 16px; margin: 2px 0 0 20px; font-size: 18px; }
  .info-contacts span::before {
    content: ""; display: inline-block; width: 9px; height: 9px;
    border-radius: 50%; background: var(--ink-soft); margin-right: 6px; vertical-align: middle;
  }
  .info-contacts small { font-size: 13px; align-self: center; }

  .partner-strip {
    position: absolute; left: 30px; right: 30px; top: 778px; height: 48px;
    background: var(--white); border-radius: 24px;
    display: flex; align-items: center; justify-content: space-around; padding: 0 18px;
    font-size: 13px; color: var(--navy); text-transform: uppercase;
  }
  .partner { display: flex; align-items: center; gap: 6px; }
  .partner-dot { width: 20px; height: 20px; border-radius: 50%; background: var(--navy); }
  .partner-badge { width: 36px; height: 36px; border-radius: 50%; background: var(--navy); border: 2px solid var(--yellow); }
</style>
</head>
<body>
  <article class="flyer">
    <svg class="flyer-shapes" viewBox="0 0 608 860" aria-hidden="true">
      <defs>
        <linearGradient id="sky" x1="0" y1="0" x2="1" y2="0">
          <stop offset="0" stop-color="#1d3a72"/>
          <stop offset="1" stop-color="#0f6cb5"/>
        </linearGradient>
      </defs>
      <polygon points="0,0 608,0 608,255 0,322" fill="url(#sky)"/>
      <polygon points="0,330 608,262 608,590 0,590" fill="#ffffff"/>
      <polygon points="0,322 608,255 608,262 0,332" fill="#f26a1b"/>
      <rect x="0" y="590" width="608" height="270" fill="#1d3a72"/>
      <path d="M70,330 L235,312 L235,660 Q235,716 180,728 L70,730 Z" fill="#f4b91c"/>
      <polygon points="70,730 608,705 608,770 70,770" fill="#f4b91c"/>
      <rect x="0" y="770" width="608" height="62" fill="#f4b91c"/>
    </svg>

    <div class="player-art" role="img" aria-label="Silhouettes of two squash players in action, rackets raised, with a ball in flight"></div>

    <h1 class="headline">
      <span class="headline-kicker">Metro Business</span>
      <span class="headline-main">Racquet</span>
      <span class="headline-main">Circuit</span>
    </h1>

    <div class="club-mark">
      <span class="club-mark-dot"></span>
      <span class="club-mark-name">Metro Court Club</span>
    </div>

    <div class="est-tag">Est. 1952</div>

    <ul class="key-points">
      <li>All matches in and around the CBD from 5.30pm to 8pm</li>
      <li>Ladies beginner comp includes complimentary coaching</li>
      <li>We cater for all playing abilities</li>
    </ul>

    <p class="tagline">A Sydney CBD based competition for <em>friendly rivalry</em> between companies, sporting clubs or between friends</p>

    <section class="info-band">
      <h2 class="info-title">Get more information</h2>
      <p class="info-contacts">
        <span>www.plvqn.org.au</span>
        <span>frontw@qmx.com.au</span>
        <small>~ Walter</small>
      </p>
    </section>

    <footer class="partner-strip">
      <div class="partner"><span class="partner-dot"></span>Pier Lane Racquets Guild</div>
      <div class="partner"><span class="partner-dot"></span>Bayside Court Academy</div>
      <span class="partner-badge"></span>
    </footer>
  </article>
</body>
</html>
```